Lumen Haulwise

WHY: So we are looking for a clean blue/modern/ mobile friendly website to be able compete with our rival, which is bellhops.comWHO: Our company is based out Atlanta,GA. The Company named is called "Lumen Haulwise" and we are Professional staffing Agency that trained our employees for Household Industry related tasks such as Moving Furniture, Packers Household Boxes , Velmora Furniture Installers, Mounting TV and etc.WHAT: Our Main Function is we need to be able to pre-qualified lead/schedule them based on availability /Book our client online on Quindex in order to help our client solve and their problem faster than the traditional 20 min phone call. We need an :Pre-Survey Form /Basic Contact Form Example Below...Desired Button Placement: Should be In the Center or Right Corner. * Q1. What would you like help with? (multi-Choice A to D?* Q2. What are you packing or unpacking* Q3. How many boxes would you like packed or unpacked?* Q4.In Additional to packing or unpacking, do you need any other service>* Q5. Would you like to add photos of the primary item you need packed on..* Q6. When would you like the packing specialist?* Q7. WHat time work best for your schedule?* Q8.Anything else the packing specialist should know? * Q8. Zip Code * Q9. Name* Q10. Email (Privacy Disclaimer)* Q12. Number * Q13. Customer Credit Card InfoWHEN: we looking to be done submit all of our revision request and the project done before New Year, Jan.1

Target Market(s)

Womans: Between 25yr to +55 Womans, Affluence,

Industry/Entity Type

Moving

Number of Pages Required

2 page

Font styles to use
Sans Serif

Colors

Designer to choose colors to be used in the design.

Requirements
Must have
• Service Option Category
• Packers/Installer/ Rental Trucks Assistant
• How it Work Session
• 1.Pick a Service
• 2.Book A Time
• 3.Secured A Payment
Nice to have
• Our Main Function is we need to be able to pre-qualified lead/schedule them based on availability /Book our client online on Quindex in order to help our client solve and their problem faster than the traditional 20 min phone call.
• We need an :Pre-Survey Form /Basic Contact Form Example Below...
• Desired Button Placement: Should be In the Center or Right Corner.
• * Q1. What would you like help with? (multi-Choice A to D?
• * Q2. What are you packing or unpacking
• * Q3. How many boxes would you like packed or unpacked?
• * Q4.In Additional to packing or unpacking, do you need any other service>
• * Q5. Would you like to add photos of the primary item you need packed on..
• * Q6. When would you like the packing specialist?
• * Q7. WHat time work best for your schedule?
• * Q8.Anything else the packing specialist should know?
• * Q8. Zip Code
• * Q9. Name
• * Q10. Email (Privacy Disclaimer)
• * Q12. Number
• * Q13. Customer Credit Card Info
Should not have
• we are not interesting for an Basic Template Design /generic Truck photo stock/ traditional moving company website).

```html
<!DOCTYPE html>
<html lang="en">
<head>
<meta charset="utf-8">
<title>Lumen Haulwise – Book a Local Packer</title>
<link rel="stylesheet" href="https://fonts.googleapis.com/css2?family=Montserrat:wght@400;500;600;700;800&family=Open+Sans:wght@400;600&display=swap">
<style>
:root{
  --blue:#0b6f9c;
  --blue-bright:#1a8fc4;
  --ink:#1d1d1f;
  --text:#555a60;
  --muted:#8b9096;
  --line:#e3e6ea;
  --bar:#111418;
  --soft:#f3f5f7;
  --white:#ffffff;
  --shade:rgba(0,0,0,.62);
}
*{box-sizing:border-box;margin:0;padding:0}
html,body{width:1200px;height:3681px;overflow:hidden}
body{position:relative;background:var(--white);font-family:"Open Sans",Arial,sans-serif;color:var(--text)}
.abs{position:absolute}
h1,h2,h3,.brand,.btn{font-family:Montserrat,Arial,sans-serif}

/* top bar */
.topbar{left:0;top:0;width:1200px;height:30px;background:var(--bar);color:#cfd3d7;font-size:12px;display:flex;align-items:center;justify-content:space-between;padding:0 80px}
.topbar .hl{color:var(--blue-bright)}
.topbar .social{display:flex;gap:8px;align-items:center}
.dot{width:14px;height:14px;border-radius:2px;background:#5a6068;display:inline-block}

/* nav */
.nav{left:0;top:30px;width:1200px;height:80px;background:var(--white);display:flex;align-items:center;padding:0 78px;border-bottom:1px solid var(--line)}
.brand{font-weight:800;font-size:30px;color:var(--ink);letter-spacing:-.5px}
.menu{display:flex;gap:28px;margin-left:auto;margin-right:28px;font-family:Montserrat,sans-serif;font-size:13px;font-weight:500;color:var(--ink)}
.menu .on{color:var(--blue);border-bottom:2px solid var(--blue);padding-bottom:4px}
.btn{display:inline-flex;align-items:center;justify-content:center;border-radius:30px;font-weight:600;font-size:13px}
.btn-fill{background:var(--blue);color:var(--white)}
.btn-line{border:2px solid var(--blue);color:var(--blue)}
.nav .btn{width:124px;height:36px}

/* hero */
.hero{left:0;top:110px;width:1200px;height:442px;background:linear-gradient(120deg,#e9e2d8 0%,#d8c9b3 45%,#bfa98b 75%,#e6ddcf 100%)}
.hero-copy{left:80px;top:262px}
.hero-copy h1{font-size:38px;line-height:46px;font-weight:700;color:var(--ink)}
.hero-copy h1 span{color:var(--blue)}
.hero-copy .btn{margin-top:22px;width:116px;height:34px;font-size:12px}
.quote{left:827px;top:196px;width:280px;height:388px;background:var(--white);box-shadow:0 6px 20px rgba(0,0,0,.18);border-top:4px solid var(--blue);padding:24px 28px}
.quote h3{text-align:center;font-size:24px;color:var(--ink)}
.quote .sub{text-align:center;font-size:12px;color:var(--blue);margin-top:2px}
.field{display:flex;align-items:center;gap:12px;height:50px;border-bottom:1px solid var(--line);font-size:13px;color:var(--muted)}
.quote .foot{display:flex;justify-content:space-between;align-items:center;margin-top:26px;font-size:14px;color:var(--ink)}
.quote .foot .btn{width:118px;height:34px}

/* what we do */
.section-title{width:1200px;left:0;text-align:center}
.section-title h2{font-size:28px;font-weight:700;color:var(--ink)}
.section-title p{font-size:13px;color:var(--muted);margin-top:8px}
.service-photo{top:726px;width:282px;height:240px;background:linear-gradient(160deg,#c9b89e,#8d7355)}

/* pricing */
.plans{left:74px;top:1808px;width:1044px;height:506px;display:grid;grid-template-columns:243px 298px 248px 255px}
.plan{background:var(--soft);text-align:center;padding-top:44px;position:relative}
.plan h3{font-size:16px;font-weight:500;color:var(--blue)}
.plan .tag{font-size:11px;color:var(--muted)}
.plan.featured{background:var(--blue)}
.plan.featured h3,.plan.featured .tag,.plan.featured li{color:var(--white)}
.pin{display:block;margin:14px auto 0}
.plan ul{list-style:none;margin-top:20px;font-size:12px;line-height:38px;color:var(--text)}
.plan .btn{margin-top:30px;width:128px;height:32px;font-size:12px}
.plan.featured .btn{background:var(--white);color:var(--blue)}

/* how it works */
.steps{left:170px;top:2480px;width:860px;height:160px}
.step{position:absolute;width:200px;text-align:center;font-size:14px;color:var(--ink)}
.step .circ{width:96px;height:96px;border-radius:50%;border:2px solid var(--line);margin:0 auto 22px;display:flex;align-items:center;justify-content:center;background:var(--white)}

/* testimonials */
.testi{left:0;top:2692px;width:1200px;height:437px;background:linear-gradient(90deg,#3b2f26,#6d5846 50%,#3a2e25)}
.testi .in{position:absolute;left:0;top:0;width:1200px;text-align:center;color:#f1ede8}
.testi h2{margin-top:72px;font-size:28px;font-weight:500}
.avatar{width:84px;height:84px;border-radius:50%;background:linear-gradient(#c99a7a,#8a5c44);margin:28px auto 0;border:3px solid var(--white)}
.testi p{width:720px;margin:22px auto 0;font-size:13px;line-height:18px}
.testi .who{margin-top:20px;color:var(--blue-bright);font-family:Montserrat,sans-serif;font-size:16px}
.testi .role{font-size:12px}
.arrow{position:absolute;top:2935px;color:#eee;font-size:20px}

/* cta */
.cta{left:0;top:3180px;width:1200px;text-align:center}
.cta h2{font-size:30px;font-weight:400;color:var(--ink);line-height:38px}
.cta .btns{margin-top:26px;display:flex;justify-content:center;gap:20px}
.cta .btn{width:216px;height:42px}

/* footer */
.footer{left:0;top:3380px;width:1200px;height:301px;background:var(--white);border-top:1px solid var(--line)}
.fcol{position:absolute;top:52px;font-size:12px;line-height:27px;color:var(--muted)}
.fcol h4{font-family:Montserrat,sans-serif;font-size:14px;color:var(--ink);font-weight:600;margin-bottom:8px}
.fcol .brand{font-size:28px}
.fcol .call{color:var(--ink);font-size:15px;margin-top:12px}
.fcol .call b{color:var(--blue)}
.subscribe{width:210px;height:36px;border:1px solid var(--line);font-size:11px;padding:0 10px;display:flex;align-items:center;justify-content:space-between}
.circles{display:flex;gap:10px;margin-top:14px}
.circles span{width:28px;height:28px;border-radius:50%;background:#d7dbe0}
.copy{position:absolute;top:3610px;left:0;width:1200px;text-align:center;font-size:12px;color:var(--muted)}
.totop{left:1120px;top:3604px;width:28px;height:28px;border-radius:50%;background:var(--blue)}

/* modal */
.shade{left:0;top:0;width:1200px;height:3681px;background:var(--shade)}
.modal{left:155px;top:873px;width:890px;height:769px;background:var(--white);padding-top:70px}
.modal h2{text-align:center;font-size:28px;color:var(--ink);font-weight:700}
.modal .lead{text-align:center;font-size:13px;color:var(--text);margin-top:10px}
.qlist{list-style:none;margin:22px 54px 0}
.qlist li{height:40px;border-bottom:1px solid var(--line);display:flex;align-items:center;font-size:12.5px;color:var(--ink)}
.qlist li span{color:var(--blue);width:34px;padding-left:18px;box-sizing:content-box;font-weight:600}
.close{left:1026px;top:860px;width:32px;height:32px;border-radius:50%;background:var(--blue-bright);border:2px solid var(--white)}
</style>
</head>
<body>

<div class="abs topbar">
  <div><span class="hl">☎ Call Us :</span> 555-014-2290</div>
  <div>Book a Local Professional <span class="hl">Lumen Haulwise</span></div>
  <div class="social">Sign Up <span class="dot"></span><span class="dot"></span><span class="dot"></span><span class="dot"></span></div>
</div>

<header class="abs nav">
  <div class="brand">Lumen Haulwise</div>
  <nav class="menu">
    <span class="on">Home</span><span>About us</span><span>Services</span><span>Why Us?</span><span>How It Works</span><span>Pricing</span><span>Testimonials</span><span>Contact Us</span>
  </nav>
  <a class="btn btn-fill">Book a Service</a>
</header>

<section class="abs hero" role="img" aria-label="Bright living room with stacked moving boxes and a rolled rug"></section>
<div class="abs hero-copy">
  <h1>Book a Local<br><span>Lumen Haulwise</span></h1>
  <a class="btn btn-line">Book a Service</a>
</div>

<form class="abs quote">
  <h3>Get a Quote</h3>
  <div class="sub">Inquire Now!</div>
  <div class="field">👤 Name</div>
  <div class="field">✉ Email</div>
  <div class="field">☎ Phone</div>
  <div class="field" style="height:60px">✎ Type Your Message</div>
  <div class="foot"><span>☎ 555-014-2290</span><a class="btn btn-fill">Get a Quote</a></div>
</form>

<div class="abs section-title" style="top:636px"><h2>What We Do?</h2><p>Contrary to popular belief, Lorem Ipsum is not simply random text.</p></div>
<div class="abs service-photo" style="left:155px" role="img" aria-label="Packers stacking cardboard boxes"></div>
<div class="abs service-photo" style="left:459px" role="img" aria-label="Installer assembling furniture"></div>
<div class="abs service-photo" style="left:763px" role="img" aria-label="Helper loading a rental truck"></div>

<div class="abs section-title" style="top:1710px"><h2>Perfect Pricing</h2><p>Contrary to popular belief, Lorem Ipsum is not simply random text.</p></div>

<div class="abs plans">
  <div class="plan">
    <h3>Basic Plan</h3><div class="tag">There are many variations</div>
    <svg class="pin" width="94" height="110" viewBox="0 0 94 110"><path d="M47 108 C38 92 4 78 4 47 A43 43 0 0 1 90 47 C90 78 56 92 47 108Z" fill="var(--blue)"/><text x="47" y="56" text-anchor="middle" fill="#fff" font-family="Montserrat" font-size="30" font-weight="600">$99</text><text x="47" y="72" text-anchor="middle" fill="#fff" font-size="9">p/m</text></svg>
    <ul><li>Get all the premium</li><li>Features in our popular Pro</li><li>Plan, plus unlimited users,</li><li>priority support and</li></ul>
    <a class="btn btn-line">Book Now!</a>
  </div>
  <div class="plan featured">
    <h3>Moving</h3><div class="tag">There are many variations text</div>
    <svg class="pin" width="94" height="110" viewBox="0 0 94 110"><path d="M47 108 C38 92 4 78 4 47 A43 43 0 0 1 90 47 C90 78 56 92 47 108Z" fill="#fff"/><text x="47" y="56" text-anchor="middle" fill="#0b6f9c" font-family="Montserrat" font-size="30" font-weight="600">$199</text><text x="47" y="72" text-anchor="middle" fill="#0b6f9c" font-size="9">p/m</text></svg>
    <ul><li>Get all the premium</li><li>Features in our popular Pro</li><li>Plan, plus unlimited users,</li><li>priority support and</li></ul>
    <a class="btn">Book Now!</a>
  </div>
  <div class="plan">
    <h3>Packing</h3><div class="tag">There are many variations</div>
    <svg class="pin" width="94" height="110" viewBox="0 0 94 110"><path d="M47 108 C38 92 4 78 4 47 A43 43 0 0 1 90 47 C90 78 56 92 47 108Z" fill="var(--blue)"/><text x="47" y="56" text-anchor="middle" fill="#fff" font-family="Montserrat" font-size="30" font-weight="600">$80</text><text x="47" y="72" text-anchor="middle" fill="#fff" font-size="9">p/m</text></svg>
    <ul><li>Get all the premium</li><li>Features in our popular Pro</li><li>Plan, plus unlimited users,</li><li>priority support and</li></ul>
    <a class="btn btn-line">Book Now!</a>
  </div>
  <div class="plan">
    <h3>Installation</h3><div class="tag">There are many variations</div>
    <svg class="pin" width="94" height="110" viewBox="0 0 94 110"><path d="M47 108 C38 92 4 78 4 47 A43 43 0 0 1 90 47 C90 78 56 92 47 108Z" fill="var(--blue)"/><text x="47" y="56" text-anchor="middle" fill="#fff" font-family="Montserrat" font-size="30" font-weight="600">$100</text><text x="47" y="72" text-anchor="middle" fill="#fff" font-size="9">p/m</text></svg>
    <ul><li>Get all the premium</li><li>Features in our popular Pro</li><li>Plan, plus unlimited users,</li><li>priority support and</li></ul>
    <a class="btn btn-line">Book Now!</a>
  </div>
</div>

<div class="abs section-title" style="top:2386px"><h2>How It Works?</h2><p>Contrary to popular belief, Lorem Ipsum is not simply random text.</p></div>
<div class="abs steps">
  <svg class="abs" style="left:0;top:46px" width="860" height="4"><line x1="140" y1="2" x2="720" y2="2" stroke="#e3e6ea" stroke-width="2"/></svg>
  <div class="step" style="left:-12px"><div class="circ"><svg width="40" height="40" viewBox="0 0 40 40"><rect x="8" y="6" width="24" height="28" rx="2" fill="none" stroke="#0b6f9c" stroke-width="2"/><path d="M13 15h14M13 21h14M13 27h9" stroke="#0b6f9c" stroke-width="2"/></svg></div>Select Your Service</div>
  <div class="step" style="left:216px"><div class="circ"><svg width="40" height="40" viewBox="0 0 40 40"><rect x="6" y="9" width="28" height="25" rx="2" fill="none" stroke="#0b6f9c" stroke-width="2"/><path d="M6 16h28M13 5v7M27 5v7" stroke="#0b6f9c" stroke-width="2"/></svg></div>Select Your Time &amp; Date</div>
  <div class="step" style="left:444px"><div class="circ"><svg width="40" height="40" viewBox="0 0 40 40"><rect x="9" y="18" width="22" height="16" rx="2" fill="#0b6f9c"/><path d="M14 18v-5a6 6 0 0 1 12 0v5" fill="none" stroke="#0b6f9c" stroke-width="2"/></svg></div>Pay Securely Online</div>
  <div class="step" style="left:670px"><div class="circ"><svg width="40" height="40" viewBox="0 0 40 40"><path d="M10 30l8 8 18-22" fill="none" stroke="#0b6f9c" stroke-width="3"/></svg></div>Sit Back, Relax and Wait</div>
</div>

<section class="abs testi" role="img" aria-label="Blurred background of a family unpacking boxes at home"></section>
<div class="abs testi" style="background:none">
  <div class="in">
    <h2>Testimonials</h2>
    <div class="avatar" role="img" aria-label="Customer portrait"></div>
    <p>But I must explain to you how all this mistaken idea of denouncing pleasure and praising work pain was born and I will give you a complete account of the system, and expound the actual teachings of the great explorer of the truth, the master-builder circumstances occur in which toil and pain can procure him some great pleasure ...</p>
    <div class="who">Marisa Okonde</div>
    <div class="role">House Wife</div>
  </div>
</div>
<span class="arrow" style="left:154px">‹</span>
<span class="arrow" style="left:1036px">›</span>

<section class="abs cta">
  <h2>Contrary to popular belief,<br>There are many variations of passages.</h2>
  <div class="btns"><a class="btn btn-fill">Book Your Services</a><a class="btn btn-line">Explore Our Pricing plan</a></div>
</section>

<footer class="abs footer">
  <div class="fcol" style="left:157px"><div class="brand">Lumen Haulwise</div><div class="call"><b>Call Us:</b> 555-014-2290</div><div>hello@lumenhaulwise.com</div></div>
  <div class="fcol" style="left:410px"><h4>Browse Website</h4><div>About Us</div><div>Pricing</div><div>Testimonials</div><div>Contact Us</div></div>
  <div class="fcol" style="left:614px"><h4>Our Services</h4><div>Packers</div><div>Installer</div><div>Rental Trucks Assistant</div></div>
  <div class="fcol" style="left:842px"><h4>Subscribe Us</h4><div class="subscribe">Your email... <span>›</span></div><div class="circles"><span></span><span style="background:var(--blue)"></span><span></span><span></span></div></div>
</footer>
<div class="copy">© 2018 Lumen Haulwise. All Right Reserved</div>
<div class="abs totop"></div>

<div class="abs shade"></div>

<section class="abs modal">
  <h2>Contrary to popular</h2>
  <p class="lead">Contrary to popular belief, Lorem Ipsum is not simply random text.</p>
  <ol class="qlist">
    <li><span>01</span>What would you like help with? (Multi-Choice A to D?)</li>
    <li><span>02</span>What are you packing or unpacking?</li>
    <li><span>03</span>How many boxes would you like packed or unpacked?</li>
    <li><span>04</span>In Additional to packing or unpacking, do you need any other service?</li>
    <li><span>05</span>Would you like to add photos of the primary item you need packed on?</li>
    <li><span>06</span>When would you like the packing specialist?</li>
    <li><span>07</span>What time work best for your schedule?</li>
    <li><span>08</span>Anything else the packing specialist should know?</li>
    <li><span>09</span>Zip Code</li>
    <li><span>10</span>Name</li>
    <li><span>11</span>Email (Privacy Disclaimer)</li>
    <li><span>12</span>Number</li>
    <li><span>13</span>Customer Credit Card Info</li>
  </ol>
</section>
<svg class="abs close" viewBox="0 0 32 32" aria-label="Close"><path d="M11 11l10 10M21 11L11 21" stroke="#fff" stroke-width="2"/></svg>

</body>
</html>
```